Watch brand needs new business cards

Kestrel Timepiece Company are looking for a new business card design incorporating our logo and brand colours as per our website.

Design should be 90x55mm with 3mm print margin from edges and 3mm external bleed.

Card should be double sided, e.g. logo one side, personal details on the other.

Logo will be provided as a vector.

The card must be able to show:
- Staff name
- Position
- Office Address
- Email
- Telephone number
- Website address

Final work must be provided in an editable format to allow us to add staff details (e.g. an AI or PSD file).

```html
<!DOCTYPE html>
<html lang="en">
<head>
<meta charset="UTF-8">
<title>Kestrel Timepiece Company – Business Cards</title>
<link rel="stylesheet" href="https://fonts.googleapis.com/css2?family=Cinzel:wght@600&family=Montserrat:wght@400;500;800&display=swap">
<style>
  :root {
    --page: #ffffff;
    --card: #000000;
    --ink: #ffffff;
    --stripe: #4a4a4a;
    --mark-faint: #3a3a3a;
  }
  * { margin: 0; padding: 0; box-sizing: border-box; }
  html, body { width: 1200px; height: 900px; overflow: hidden; background: var(--page); }
  .canvas { position: relative; width: 1200px; height: 900px; font-family: "Montserrat", sans-serif; color: var(--ink); }

  .card { position: absolute; left: 341px; width: 520px; height: 317px; background: var(--card); overflow: hidden; }
  .card--front { top: 100px; }
  .card--back { top: 469px; }

  .stripes { position: absolute; width: 28px; height: 156px; display: flex; justify-content: space-between; }
  .stripes span { display: block; width: 6px; height: 100%; background: var(--stripe); }
  .stripes--left { left: 0; }
  .stripes--right { right: 0; }
  .card--front .stripes { top: 81px; }
  .card--back .stripes { top: 80px; }

  .brand-circle { position: absolute; left: 215px; top: 83px; }
  .brand-name { position: absolute; left: 0; top: 181px; width: 100%; text-align: center; font-family: "Cinzel", serif; font-weight: 600; line-height: 1; }
  .brand-name__main { display: block; font-size: 42px; letter-spacing: 1px; }
  .brand-name__sub { display: block; font-size: 14px; letter-spacing: 2.5px; margin-top: 5px; }

  .back-ring { position: absolute; left: 45px; top: 27px; }

  .rotated { position: absolute; transform: rotate(-90deg); transform-origin: center; }
  .staff { left: 270px; top: 132px; width: 160px; height: 52px; text-align: center; }
  .staff__name { font-weight: 800; font-size: 20px; line-height: 25px; letter-spacing: 0.5px; }
  .staff__position { font-size: 16px; line-height: 22px; }

  .contact { left: 350px; top: 125px; width: 160px; height: 72px; text-align: right; list-style: none; font-size: 11px; line-height: 18px; }

  .social { position: absolute; left: 396px; top: 223px; display: flex; gap: 6px; }
  .social span { width: 11px; height: 11px; border-radius: 50%; background: var(--ink); }
</style>
</head>
<body>
<main class="canvas">
  <section class="card card--front" aria-label="Business card front">
    <div class="stripes stripes--left"><span></span><span></span><span></span></div>
    <svg class="brand-circle" width="88" height="88" viewBox="0 0 88 88" aria-hidden="true">
      <circle cx="44" cy="44" r="40" fill="none" stroke="var(--ink)" stroke-width="4"/>
    </svg>
    <h1 class="brand-name">
      <span class="brand-name__main">KESTREL</span>
      <span class="brand-name__sub">TIMEPIECE COMPANY</span>
    </h1>
    <div class="stripes stripes--right"><span></span><span></span><span></span></div>
  </section>

  <section class="card card--back" aria-label="Business card back">
    <div class="stripes stripes--left"><span></span><span></span><span></span></div>
    <svg class="back-ring" width="270" height="270" viewBox="0 0 270 270" aria-hidden="true">
      <circle cx="135" cy="135" r="128" fill="none" stroke="var(--mark-faint)" stroke-width="10"/>
    </svg>
    <div class="rotated staff">
      <p class="staff__name">STAFF NAME</p>
      <p class="staff__position">Position</p>
    </div>
    <ul class="rotated contact">
      <li>A5 Office Address</li>
      <li>staff@kestrel.com</li>
      <li>+91 312456789</li>
      <li>www.website.co.in</li>
    </ul>
    <div class="social" aria-hidden="true"><span></span><span></span><span></span><span></span></div>
    <div class="stripes stripes--right"><span></span><span></span><span></span></div>
  </section>
</main>
</body>
</html>
```